Rent a Velvet needs a Stunning web design

Rent a Velvet is an upmarket agency in Sydney that has lingerie waitresses for events.

Rent a Velvet is looking for a website design that is as sexy and sophisticated as the ladies who work for them!

The design mustn't be cluttered, tacky or pornographic. What I'm looking for is something better than the industry leader www.glimmerdolls.com.au Something classy, sexy and different.

When designing please suggest a CMS, we already use wordpress but are open to suggestions.

We will need a home page that incorporates a feed from a blog and/or social media (please make suggestions and use your discretion as a designer, however we'd like to approve what goes into the feed before it goes in.) The home page could also have a list of our services, but if not we will need a services page. Our Services include:
Lingerie waitressing at events
Lingerie waitresses to help dress the groom pre wedding.
Bucks parties

We have a logo that we'd like incorporated into the design and have attached it.

We will also need a portfolio page for the ladies, This is not to be cluttered, tacky or pornographic. It needs to be classy.

We will also need a "Contact us" page and were thinking that this could potentially also be a "Ask for a quote on your event" page. I.e. have a regular "Contact us" form but have alternate fields if they tick the "I want a quote" box. Alternatively you could have two parts to the contact us page. One that is a regular form and one that has a "Your requirements" box.

Again please use your discretion when designing these, if it's too cluttered it won't work. If it looks tacky, don't do it. If you have suggestions make them.

Target Market(s)

Males between the ages of 18 - 45

Industry/Entity Type

Industry

Requirements
Must have
• Must incorporate our logo.

```html
<!DOCTYPE html>
<html lang="en">
<head>
<meta charset="utf-8">
<title>Rent a Velvet</title>
<link rel="stylesheet" href="https://fonts.googleapis.com/css2?family=Cinzel:wght@400;600;700&family=Josefin+Sans:wght@400;600&family=Montserrat:wght@300;700;800&display=swap">
<style>
  :root {
    --page: #f4f2f0;
    --blush: #f2dde6;
    --ink: #1e1a1c;
    --plum: #5b2d45;
    --pink: #d667b0;
    --pink-light: #f0a9d8;
    --pink-dark: #b84b93;
    --panel: #ffffff;
    --panel-edge: #e3dee0;
    --services-bg: #efeded;
    --rule: #d4cfd0;
    --footer-rule: #d8d0c2;
  }
  * { box-sizing: border-box; margin: 0; padding: 0; }
  html, body { width: 1200px; height: 1057px; overflow: hidden; }
  body {
    position: relative;
    background:
      radial-gradient(ellipse 700px 260px at 600px 760px, var(--blush), transparent 70%),
      var(--page);
    color: var(--ink);
    font-family: "Josefin Sans", sans-serif;
  }
  .brand {
    position: absolute; left: 131px; top: 62px;
    display: flex; align-items: center; gap: 12px;
    font-family: "Cinzel", serif; font-weight: 700; font-size: 30px; color: var(--ink);
  }
  .brand-dot { width: 18px; height: 18px; border-radius: 50%; background: var(--ink); }
  .social {
    position: absolute; left: 776px; top: 110px;
    display: flex; align-items: center; gap: 7px;
    font-family: "Montserrat", sans-serif; font-weight: 700; font-size: 9px; letter-spacing: -0.2px; color: #2d3550;
  }
  .social-square { width: 16px; height: 16px; background: #5f84c4; border-radius: 2px; }
  .social-square.alt { background: #4ab4e4; }
  .social-label { margin-left: 6px; }
  .address {
    position: absolute; left: 898px; top: 62px;
    font-family: "Cinzel", serif; font-size: 9.5px; letter-spacing: 1.2px; line-height: 17.5px; color: var(--ink);
  }
  .nav {
    position: absolute; left: 114px; top: 153px; width: 948px; height: 37px;
    background: linear-gradient(var(--pink-light), var(--pink) 55%, var(--pink-dark));
    border: 2px solid #f7c6e3;
    display: flex;
  }
  .nav a {
    display: flex; align-items: center; justify-content: center;
    color: #fff; text-decoration: none;
    font-family: "Cinzel", serif; font-size: 12.5px;
    border-right: 1px solid rgba(255,255,255,0.5);
  }
  .nav a:last-child { border-right: none; }
  .hero-panel {
    position: absolute; left: 114px; top: 199px; width: 948px; height: 425px;
    background: var(--panel); border: 1px solid var(--panel-edge);
    box-shadow: 0 0 6px rgba(0,0,0,0.06);
  }
  .services {
    position: absolute; left: 13px; top: 10px; width: 252px; height: 404px;
    background: linear-gradient(90deg, var(--services-bg), #f8f8f8);
    text-align: center;
  }
  .services h2 {
    font-family: "Cinzel", serif; font-weight: 400; font-size: 16px; letter-spacing: 3px;
    padding-top: 16px; height: 55px; color: var(--ink);
  }
  .services ul { list-style: none; }
  .services li {
    margin: 0 24px; border-top: 1px solid var(--rule);
    display: flex; align-items: center; justify-content: center;
    font-size: 9.5px; font-weight: 600; letter-spacing: 1.6px; line-height: 17px;
    color: var(--plum); text-transform: uppercase;
  }
  .services li.wide { margin: 0 4px; }
  .services li.wide-rule { border-top: none; }
  .services .more {
    display: inline-block; margin-top: 12px;
    font-size: 12px; letter-spacing: 2.2px; color: var(--plum); text-decoration: underline;
  }
  .hero-photo { position: absolute; top: 10px; height: 404px; }
  .photo-a { left: 277px; width: 211px; background: linear-gradient(160deg, #e2e2e2, #9a9a9a 60%, #3a3a3a); }
  .photo-b { left: 488px; width: 222px; background: linear-gradient(160deg, #3d3230, #a8786a 45%, #e9dcd4); }
  .photo-c { left: 710px; width: 226px; background: linear-gradient(160deg, #6a6a6a, #2b2b2b 55%, #4c4c4c); }
  .hero-tag {
    position: absolute; left: 575px; top: 272px; width: 361px; height: 85px;
    background: linear-gradient(90deg, rgba(214,103,176,0.3), rgba(214,103,176,0.75));
    text-align: right; padding: 12px 22px 0 0; color: #fff; font-family: "Montserrat", sans-serif;
  }
  .hero-tag .small { font-weight: 800; font-size: 17px; letter-spacing: -0.3px; }
  .hero-tag .big { font-weight: 800; font-size: 37px; line-height: 40px; letter-spacing: 0.5px; }
  .tile {
    position: absolute; top: 632px; height: 155px; background: var(--panel);
    border: 1px solid var(--panel-edge); box-shadow: 0 0 6px rgba(0,0,0,0.06);
  }
  .tile-media { position: absolute; left: 7px; top: 7px; right: 7px; bottom: 7px; }
  .tile-shows { left: 115px; width: 305px; }
  .tile-gallery { left: 436px; width: 305px; }
  .tile-map { left: 757px; width: 305px; }
  .shows-media { background: linear-gradient(120deg, #6a4a2a, #c9a889 45%, #e9dccd 70%, #8d6b46); }
  .gallery-media { background: linear-gradient(100deg, #2a1e1a, #7a5646 40%, #c79a84 70%, #2e221e); }
  .map-media { background: #e6e1d5; }
  .tile-label {
    position: absolute; color: #fff; font-family: "Montserrat", sans-serif; text-align: center;
  }
  .shows-label { left: 20px; top: 71px; width: 245px; }
  .shows-label .top { display: block; background: rgba(214,103,176,0.75); font-weight: 800; font-size: 17px; height: 31px; line-height: 31px; }
  .shows-label .bottom { display: block; background: rgba(30,20,20,0.75); font-weight: 300; font-size: 18px; height: 32px; line-height: 32px; }
  .gallery-label { left: 30px; top: 100px; width: 245px; height: 31px; line-height: 31px; background: rgba(214,103,176,0.75); font-weight: 800; font-size: 17px; }
  .map-label { left: 34px; top: 100px; width: 245px; height: 32px; line-height: 32px; background: rgba(214,103,176,0.75); font-weight: 800; font-size: 17px; }
  .pin { position: absolute; left: 162px; top: 86px; }
  .footer-rule { position: absolute; left: 120px; top: 840px; width: 934px; border-top: 1px solid var(--footer-rule); }
  .footer-nav { position: absolute; top: 858px; left: 0; width: 1200px; height: 20px; }
  .footer-nav a, .cities span {
    position: absolute; font-family: "Cinzel", serif; font-size: 12px; color: var(--ink); text-decoration: none; white-space: nowrap;
  }
  .cities { position: absolute; top: 904px; left: 0; width: 1200px; height: 16px; }
  .cities span { font-size: 10.5px; }
  .footer-brand {
    position: absolute; left: 0; top: 970px; width: 1200px; text-align: center;
    font-family: "Cinzel", serif; font-weight: 700; font-size: 24px; color: var(--ink);
  }
</style>
</head>
<body>
  <header>
    <div class="brand"><span class="brand-name">Rent a Velvet</span><span class="brand-dot"></span></div>
    <div class="social">
      <span class="social-square"></span><span class="social-square alt"></span><span class="social-label">FOLLOW US</span>
    </div>
    <address class="address">
      5/F ASTER HOUSE<br>24-26 HARBOUR LANE<br>CENTRAL, GOLD COAST<br>MARA QUINN
    </address>
    <nav class="nav">
      <a href="#" style="width:131px">Home</a>
      <a href="#" style="width:184px">Services</a>
      <a href="#" style="width:158px">Girls Gallery</a>
      <a href="#" style="width:139px">What we do</a>
      <a href="#" style="width:169px">About us</a>
      <a href="#" style="width:163px">Contact Us</a>
    </nav>
  </header>

  <main>
    <section class="hero-panel">
      <div class="services">
        <h2>SERVICES</h2>
        <ul>
          <li style="height:70px">Lingerie waitressing<br>at events</li>
          <li class="wide wide-rule" style="height:72px">Lingerie waitresses to help dress<br>the groom pre wedding.</li>
          <li style="height:60px">Bucks parties</li>
          <li style="height:53px">Party bus tours</li>
          <li style="height:53px">Topless poker</li>
          <li style="height:2px"></li>
        </ul>
        <a class="more" href="#">VIEW FULL LIST</a>
      </div>
      <div class="hero-photo photo-a" role="img" aria-label="Black and white photo of a model in lingerie"></div>
      <div class="hero-photo photo-b" role="img" aria-label="Colour photo of a model in white lingerie"></div>
      <div class="hero-photo photo-c" role="img" aria-label="Black and white photo of a model in a lace slip"></div>
      <div class="hero-tag">
        <div class="small">PRETTIEST GIRLS FOR YOUR</div>
        <div class="big">EVENTS</div>
      </div>
    </section>

    <a class="tile tile-shows" href="#">
      <div class="tile-media shows-media" role="img" aria-label="Photo of a performer in a gilded room"></div>
      <div class="tile-label shows-label"><span class="top">UPCOMING SHOWS</span><span class="bottom">IN NOVEMBER</span></div>
    </a>
    <a class="tile tile-gallery" href="#">
      <div class="tile-media gallery-media" role="img" aria-label="Photo of guests at a show"></div>
      <div class="tile-label gallery-label">VIEW SHOWS GALLERY</div>
    </a>
    <a class="tile tile-map" href="#">
      <div class="tile-media map-media" role="img" aria-label="Street map showing the agency location"></div>
      <svg class="pin" width="18" height="24" viewBox="0 0 18 24"><path d="M9 23 C4 15 1 12 1 8 A8 8 0 0 1 17 8 C17 12 14 15 9 23Z" fill="#e2675a" stroke="#a8433a"/></svg>
      <div class="tile-label map-label">FIND US</div>
    </a>
  </main>

  <footer>
    <div class="footer-rule"></div>
    <nav class="footer-nav">
      <a href="#" style="left:169px">Home</a>
      <a href="#" style="left:305px">Services</a>
      <a href="#" style="left:445px">Girls Gallery</a>
      <a href="#" style="left:584px">What we do</a>
      <a href="#" style="left:731px">About us</a>
      <a href="#" style="left:878px">Contact Us</a>
    </nav>
    <div class="cities">
      <span style="left:402px">SYDNEY</span>
      <span style="left:461px">-</span>
      <span style="left:487px">MELBOURNE</span>
      <span style="left:570px">-</span>
      <span style="left:598px">BRISBANE</span>
      <span style="left:666px">-</span>
      <span style="left:692px">GOLD COAST</span>
    </div>
    <div class="footer-brand">Rent a Velvet</div>
  </footer>
</body>
</html>
```